Velmora Water Purification

We need a website set up on a "Free account" WordPress platform. (This is the type of Wordpress site that you can sign up for and create online for free (not a server-hosted type.)
The website will be for a water purification company. They install devices in homes to purify the water for safer drinking, bathing, and cleaning.
Our logo is attached. Please keep color scheme of the website consistent with the logo.
Water Purification

```html
<!DOCTYPE html>
<html lang="en">
<head>
<meta charset="UTF-8">
<title>Velmora Water Purification – Our Products</title>
<link href="https://fonts.googleapis.com/css2?family=Quicksand:wght@400;500&family=Mulish:wght@400&display=swap" rel="stylesheet">
<style>
  :root {
    --accent: #8f45b8;
    --price: #9a4fc0;
    --heading: #1f2033;
    --name: #3a3a3a;
    --spec: #5a5a5a;
    --bg-top: #f8fbff;
    --bg-mid: #eef5fc;
    --bg-wave: #d6e4f3;
    --arrow: #1a1a1a;
  }
  * { margin: 0; padding: 0; box-sizing: border-box; }
  html, body { width: 1200px; height: 470px; overflow: hidden; }
  body { font-family: "Quicksand", sans-serif; background: var(--bg-top); }

  .products {
    position: relative;
    width: 1200px;
    height: 470px;
    border-top: 1px solid var(--accent);
    overflow: hidden;
  }
  .products__backdrop {
    position: absolute; inset: 0;
    background:
      radial-gradient(ellipse 420px 120px at 900px 450px, var(--bg-wave), transparent 70%),
      radial-gradient(ellipse 300px 90px at 1150px 400px, var(--bg-wave), transparent 70%),
      linear-gradient(180deg, var(--bg-top) 0%, var(--bg-mid) 100%);
  }
  .products__title {
    position: absolute; top: 70px; left: 0; width: 100%;
    text-align: center;
    font-size: 31px; font-weight: 400;
    color: var(--heading);
  }
  .product {
    position: absolute; top: 166px;
    width: 220px; margin-left: -110px;
    text-align: center;
  }
  .product__name {
    font-size: 17px; font-weight: 400; color: var(--name);
    line-height: 22px;
  }
  .product__photo {
    width: 104px; height: 112px;
    margin: 23px auto 0;
    border-radius: 8px;
  }
  .product__spec {
    margin-top: 22px;
    font-family: "Mulish", sans-serif;
    font-size: 13px; color: var(--spec);
    line-height: 16px;
  }
  .product__price {
    margin-top: 6px;
    font-size: 16px; font-weight: 500; color: var(--price);
    line-height: 22px;
  }
  .carousel-arrow {
    position: absolute; top: 254px;
    width: 16px; height: 36px;
  }
  .carousel-arrow--prev { left: 128px; }
  .carousel-arrow--next { left: 1055px; }
</style>
</head>
<body>
<section class="products">
  <div class="products__backdrop" role="img" aria-label="Soft pale blue water splash background"></div>

  <h2 class="products__title">Our Products</h2>

  <svg class="carousel-arrow carousel-arrow--prev" viewBox="0 0 16 36" aria-label="Previous">
    <polyline points="15,1 1,18 15,35" fill="none" stroke="var(--arrow)" stroke-width="1.2"/>
  </svg>
  <svg class="carousel-arrow carousel-arrow--next" viewBox="0 0 16 36" aria-label="Next">
    <polyline points="1,1 15,18 1,35" fill="none" stroke="var(--arrow)" stroke-width="1.2"/>
  </svg>

  <article class="product" style="left:253px">
    <h3 class="product__name">Product Name</h3>
    <div class="product__photo" role="img" aria-label="Gravity water purifier with clear blue tank and white base"
         style="background:linear-gradient(180deg,#cfe6f8 0%,#8cc4ec 55%,#e9eef2 100%)"></div>
    <p class="product__spec">RO+UV+UF+TDS Control</p>
    <p class="product__price">Price: $250.00</p>
  </article>

  <article class="product" style="left:486px">
    <h3 class="product__name">Product Name</h3>
    <div class="product__photo" role="img" aria-label="Wall-mounted water purifier with aqua front and white frame"
         style="background:linear-gradient(180deg,#eef2f4 0%,#a9e3dc 50%,#e6f2f0 100%)"></div>
    <p class="product__spec">RO+UV+UF+TDS Control</p>
    <p class="product__price">Price: $700.00</p>
  </article>

  <article class="product" style="left:721px">
    <h3 class="product__name">Product Name</h3>
    <div class="product__photo" role="img" aria-label="Black countertop water dispenser purifier"
         style="background:linear-gradient(180deg,#3a3a3c 0%,#151516 60%,#222 100%)"></div>
    <p class="product__spec">RO+UV+UF+TDS Control</p>
    <p class="product__price">Price: $950.00</p>
  </article>

  <article class="product" style="left:954px">
    <h3 class="product__name">Product Name</h3>
    <div class="product__photo" role="img" aria-label="Teal wall-mounted water purifier with grey front panel"
         style="background:linear-gradient(90deg,#2bb5bd 0%,#3ec2c8 30%,#b9c4cc 50%,#3ec2c8 70%,#2aa9b2 100%)"></div>
    <p class="product__spec">RO+UV+UF+TDS Control</p>
    <p class="product__price">Price: $450.00</p>
  </article>
</section>
</body>
</html>
```